Welcome Card Project for bow tie business

We need a welcome message card that will be placed inside a box (packaging) for a mens bow tie business 'Howard Vance'. Howard Vance is a men's brand specializing in unique bow ties of limited editions using quality designer fabrics.
Howard Vance is all about colour, prints and style, where the consumer can add a something a little out of the ordinary and quirky to break out of the mundane 9-5 day.

The dimensions of the double sided welcome card is as follows:
60mm H x 120mm W

One side of the welcome card will have the welcome message with colour and graphics in the background depicting happiness and excitement. It will also include the Chatterly, chirpnet and Snapvue logos and an invitation for customers to share pictures of them wearing the bow ties on Snapvue and chatterly. The website address will also be included here (www.howardvance.example)

The other side of the welcome card will be more conservative with a black on black paisley print design with the 'Howard Vance' logo in a deep purple colour.

Target Market(s)

Men, hipsters, fashionistas, working professionals, women seeking gifts for men

Industry/Entity Type

Conservative

Requirements
Must have
• - Double sided welcome card
- The welcome message (file attached) on one side of the card
- Chatterly + Snapvue logo
- Howard Vance website address (www.howardvance.example)
- Corporate colours: purple, black, orange (on website and in logo) + neutral recycled brown (packaging colour)
- Black on black paisley print on one side of the card
- Howard Vance logo (file attached)- colour: deep purple
Nice to have

Should not have
• - pictures of rainbows

```html
<!DOCTYPE html>
<html lang="en">
<head>
<meta charset="utf-8">
<title>Howard Vance – Welcome Card</title>
<link href="https://fonts.googleapis.com/css2?family=Playfair+Display:wght@400&family=Crimson+Pro:wght@700&family=Oswald:wght@500&display=swap" rel="stylesheet">
<style>
  :root {
    --page: #ffffff;
    --border-a: #f05a7c;
    --border-b: #d8446c;
    --panel-left: #ff5a70;
    --panel-right: #ff2f5f;
    --deep-purple: #5c0f4c;
    --wine: #a3102c;
    --white: #ffffff;
    --ornament: rgba(92, 15, 76, 0.45);
  }
  * { margin: 0; padding: 0; box-sizing: border-box; }
  html, body { width: 1115px; height: 1200px; overflow: hidden; background: var(--page); }
  .canvas { position: relative; width: 1115px; height: 1200px; }

  .card { position: absolute; left: 117px; width: 886px; height: 465px; }
  .card--message { top: 60px; }
  .card--brand { top: 638px; }

  .card__border {
    position: absolute; inset: 0;
    background: linear-gradient(90deg, var(--border-a), var(--border-b) 30%, var(--border-a) 55%, var(--border-b) 80%, var(--border-a));
  }
  .card__panel {
    position: absolute; left: 33px; top: 35px; width: 818px; height: 395px;
    border-radius: 32px;
    background: linear-gradient(90deg, var(--panel-left), #ff5c72 50%, var(--panel-right));
  }

  .rule { position: absolute; height: 3px; background: var(--deep-purple); }
  .rule--top { left: 108px; top: 64px; width: 592px; }
  .rule--bottom { left: 196px; top: 331px; width: 429px; }

  .flourish { position: absolute; width: 78px; height: 46px; border-radius: 23px; background: var(--ornament); }
  .flourish--top { left: 363px; top: 14px; }
  .flourish--bottom { left: 366px; top: 336px; }

  .headline {
    position: absolute; left: 0; right: 0; top: 72px;
    text-align: center;
    font-family: "Playfair Display", serif; font-weight: 400;
    font-size: 37px; letter-spacing: 0.5px; color: var(--white);
  }
  .message {
    position: absolute; left: 20px; right: 20px;
    text-align: center;
    font-family: "Crimson Pro", serif; font-weight: 700;
    font-size: 21px; line-height: 31px;
  }
  .message--intro { top: 132px; color: var(--wine); }
  .message--invite { top: 207px; color: var(--deep-purple); }

  .signoff {
    position: absolute; right: 26px; top: 340px;
    font-family: "Oswald", sans-serif; font-weight: 500;
    font-size: 24px; color: var(--white);
  }

  .wordmark {
    position: absolute; left: 0; right: 0; top: 118px;
    text-align: center;
    font-family: "Crimson Pro", serif; font-weight: 700;
    font-size: 118px; color: var(--deep-purple);
  }
  .website {
    position: absolute; left: 0; right: 0; top: 332px;
    text-align: center;
    font-family: "Oswald", sans-serif; font-weight: 500;
    font-size: 21px; letter-spacing: 0.5px; color: var(--deep-purple);
  }
  .social {
    position: absolute; right: 12px; top: 337px;
    display: flex; gap: 8px; align-items: center;
    font-family: "Oswald", sans-serif; font-weight: 500;
    font-size: 13px; color: var(--deep-purple);
  }
  .social__item { display: flex; align-items: center; gap: 4px; }
  .social__dot { width: 12px; height: 12px; background: var(--deep-purple); }
</style>
</head>
<body>
<div class="canvas">

  <section class="card card--message">
    <div class="card__border" role="img" aria-label="Pink hexagon pattern border"></div>
    <div class="card__panel">
      <div class="flourish flourish--top" role="img" aria-label="Decorative flourish"></div>
      <div class="rule rule--top"></div>
      <h1 class="headline">THIS IS ONLY THE BEGINNING</h1>
      <p class="message message--intro">YOUR HOWARD VANCE BOW TIE IS AN ADVENTURE FOR YOU TO UNFOLD,<br>UNEXPECTED AND NEW.</p>
      <p class="message message--invite">WEAR IT ON A NIGHT OUT, OR BRING A DASH OF COLOUR TO WORK,<br>DREAM WITH IT, WEAR IT ON A RAINY DAY, CREATE NEW MEMORIES AND<br>BE SURPRISED.</p>
      <div class="rule rule--bottom"></div>
      <div class="flourish flourish--bottom" role="img" aria-label="Decorative flourish"></div>
      <p class="signoff">HOWARD VANCE</p>
    </div>
  </section>

  <section class="card card--brand">
    <div class="card__border" role="img" aria-label="Pink hexagon pattern border"></div>
    <div class="card__panel">
      <p class="wordmark">Howard Vance</p>
      <p class="website">WWW.HOWARDVANCE.EXAMPLE</p>
      <div class="social">
        <span class="social__item"><span class="social__dot"></span>Chatterly</span>
        <span class="social__item">Snapvue</span>
      </div>
    </div>
  </section>

</div>
</body>
</html>
```